Builders Worksite Corflute Outdoor Sign

We are a building company who are just branching out into new construction. How first new build is our own home which was designed by us and a local architect. We are proud and want to create more advertisement around our business.

We need a corflute sign that can staked outside the construction site and can be seen by people passing by.
Updates

Can we please make the company name and logo bigger (Tidewater Ridge Homes) This needs to be the focus. Can we please replace 'Manu' with 'Contact Us on 021-574-3619'

Target Market(s)

Home owners and people wishing to build on lifestyle blocks in New Zealand.

Font styles to use
Sans Serif

Requirements
Must have
• It needs to feature our:
Logo
Company name
Contact name and number - Manu - 0215743619
Landscape NOT portrait.

```html
<!DOCTYPE html>
<html lang="en">
<head>
<meta charset="utf-8">
<title>Tidewater Ridge Homes – Worksite Sign</title>
<link href="https://fonts.googleapis.com/css2?family=Bebas+Neue&family=Montserrat:wght@400&family=Saira+Condensed:wght@700;800&display=swap" rel="stylesheet">
<style>
  :root {
    --canvas: #ffffff;
    --navy: #1a2030;
    --gold: #f1bf1a;
    --gold-deep: #cf9a2a;
    --white: #ffffff;
  }
  html, body {
    margin: 0;
    padding: 0;
    width: 1200px;
    height: 960px;
    overflow: hidden;
    background: var(--canvas);
  }
  .canvas {
    position: relative;
    width: 1200px;
    height: 960px;
  }
  .sign {
    position: absolute;
    left: 66px;
    top: 138px;
    width: 1067px;
    height: 684px;
    background: var(--navy);
  }
  .brand {
    position: absolute;
    left: 0;
    right: 0;
    top: 0;
    text-align: center;
    color: var(--white);
    font-family: "Montserrat", sans-serif;
    font-weight: 400;
  }
  .brand-dot {
    position: absolute;
    left: 50%;
    top: 60px;
    width: 96px;
    height: 96px;
    margin-left: -48px;
    border-radius: 50%;
    background: var(--gold);
  }
  .brand-name {
    position: absolute;
    left: 0;
    right: 0;
    top: 195px;
    margin: 0;
    font-size: 60px;
    line-height: 1;
    letter-spacing: 1px;
    text-transform: uppercase;
    font-weight: 400;
  }
  .brand-sub {
    position: absolute;
    left: 0;
    right: 0;
    top: 280px;
    font-size: 34px;
    line-height: 1;
    letter-spacing: 0.55em;
    padding-left: 0.55em;
    text-transform: uppercase;
  }
  .name-band {
    position: absolute;
    left: 0;
    right: 0;
    top: 346px;
    height: 128px;
    background: linear-gradient(to bottom, var(--gold) 0%, var(--gold) 35%, var(--gold-deep) 100%);
    display: flex;
    align-items: center;
    justify-content: center;
  }
  .band-title {
    margin: 0;
    font-family: "Bebas Neue", sans-serif;
    font-weight: 400;
    font-size: 122px;
    line-height: 1;
    letter-spacing: 3px;
    color: var(--navy);
    white-space: nowrap;
    padding-top: 10px;
  }
  .contact {
    position: absolute;
    left: 0;
    right: 0;
    top: 496px;
    text-align: center;
    font-family: "Saira Condensed", sans-serif;
  }
  .contact-label {
    margin: 0;
    font-size: 54px;
    font-weight: 700;
    line-height: 1;
    color: var(--white);
    letter-spacing: 1px;
  }
  .contact-phone {
    display: block;
    margin-top: 12px;
    font-size: 112px;
    font-weight: 800;
    line-height: 1;
    color: var(--gold);
    letter-spacing: 3px;
    text-decoration: none;
  }
</style>
</head>
<body>
<main class="canvas">
  <section class="sign">
    <header class="brand">
      <span class="brand-dot" aria-hidden="true"></span>
      <p class="brand-name">Tidewater Ridge</p>
      <p class="brand-sub">Homes</p>
    </header>
    <div class="name-band">
      <h1 class="band-title">TIDEWATER RIDGE HOMES</h1>
    </div>
    <div class="contact">
      <p class="contact-label">Contact Us on</p>
      <a class="contact-phone" href="tel:0215743619">021-574-3619</a>
    </div>
  </section>
</main>
</body>
</html>
```